University Chair needs a Flyer for inviting participants to a Podcast series

We need a flyer design for a new podcast series. The Centre for Market Structures at the business university KLB (www.klb.edu) will invite selected contacts to participate in a new podcast series. The flyer should first gain the participants attention and interest and second inform them about the activity. The overall theme is on "Strategy, Analytics, Economics and Leadership". Please refer to the flyer.pdf in the attached files.

Industry/Entity Type

Business

Font styles to use
Serif
Sans Serif

```html
<!DOCTYPE html>
<html lang="en">
<head>
<meta charset="utf-8">
<title>Centre for Market Structures – Podcast Series Invitation</title>
<link rel="stylesheet" href="https://fonts.googleapis.com/css2?family=Open+Sans:wght@400;700&family=Noto+Sans:wght@400;600&display=swap">
<style>
  :root {
    --backdrop: #a9c9e2;
    --paper: #f3f3f4;
    --ink: #1a1d2b;
    --navy: #0b1538;
    --night: #0a0f25;
    --royal: #1b2c95;
    --cobalt: #2b46a8;
    --lavender: #6f7fbf;
    --fold-shadow: rgba(20, 30, 60, 0.10);
  }
  * { box-sizing: border-box; margin: 0; padding: 0; }
  html, body { width: 1200px; height: 900px; overflow: hidden; }
  body { background: var(--backdrop); font-family: "Open Sans", Arial, sans-serif; color: var(--ink); }

  .brochure {
    position: absolute; left: 90px; top: 60px;
    width: 1020px; height: 780px;
    display: flex;
  }
  .panel {
    position: relative; width: 340px; height: 780px;
    background: var(--paper); overflow: hidden;
  }
  .panel + .panel { box-shadow: inset 10px 0 14px -10px var(--fold-shadow); }
  .panel svg.shapes { position: absolute; inset: 0; width: 340px; height: 780px; }

  /* Panel 1: theme points */
  .point { position: absolute; left: 34px; width: 290px; display: flex; gap: 12px; align-items: flex-start; }
  .point-number { font-size: 27px; line-height: 1; font-weight: 400; width: 18px; padding-top: 1px; flex: none; }
  .point-text { font-size: 12.5px; line-height: 15px; }
  .point-text strong { font-weight: 700; }

  /* Panel 2: titled sections */
  .section { position: absolute; left: 31px; width: 278px; }
  .section-title { font-weight: 700; font-size: 23px; letter-spacing: 0.5px; margin-bottom: 6px; }
  .section-text { font-size: 12px; line-height: 15px; }

  /* Panel 3: invitation */
  .intro { position: absolute; left: 34px; top: 158px; width: 262px; font-family: "Noto Sans", Arial, sans-serif; }
  .intro-title { font-weight: 600; font-size: 21px; margin-bottom: 14px; }
  .intro-text { font-size: 12.5px; line-height: 17.3px; letter-spacing: 0.4px; }
  .intro-link { font-weight: 600; }
</style>
</head>
<body>
<main class="brochure">

  <section class="panel panel-points">
    <svg class="shapes" viewBox="0 0 340 780" aria-hidden="true">
      <polygon points="297,52 340,10 340,52" fill="var(--night)"/>
      <polygon points="196,307 343,307 343,437" fill="var(--lavender)"/>
      <polygon points="294,324 340,286 340,324" fill="var(--night)"/>
      <polygon points="0,647 0,780 150,780" fill="var(--cobalt)"/>
    </svg>
    <div class="point" style="top:125px"><span class="point-number">1</span><p class="point-text"><strong>Strategy</strong> – how leading firms choose where to compete and how to win.</p></div>
    <div class="point" style="top:215px"><span class="point-number">2</span><p class="point-text"><strong>Analytics</strong> – turning data into sound decisions, from pricing to forecasts.</p></div>
    <div class="point" style="top:476px"><span class="point-number">3</span><p class="point-text"><strong>Economics</strong> – competition, regulation and market structures in practice.</p></div>
    <div class="point" style="top:571px"><span class="point-number">4</span><p class="point-text"><strong>Leadership</strong> – guiding teams and organisations through change.</p></div>
  </section>

  <section class="panel panel-sections">
    <svg class="shapes" viewBox="0 0 340 780">
      <defs>
        <linearGradient id="campus-tones" x1="0" y1="0" x2="1" y2="1">
          <stop offset="0" stop-color="#9a9aa0"/>
          <stop offset="0.45" stop-color="#8a6a5e"/>
          <stop offset="1" stop-color="#5b4a46"/>
        </linearGradient>
        <linearGradient id="night-fade" x1="0" y1="1" x2="1" y2="0">
          <stop offset="0" stop-color="var(--night)"/>
          <stop offset="1" stop-color="#101c40"/>
        </linearGradient>
      </defs>
      <polygon points="0,475 180,640 340,640 340,780 0,780" fill="url(#campus-tones)" role="img" aria-label="Photograph of the KLB university campus building"/>
      <polygon points="340,372 35,640 340,640" fill="url(#night-fade)"/>
      <polygon points="187,444 187,525 279,525" fill="var(--cobalt)"/>
    </svg>
    <div class="section" style="top:58px">
      <h2 class="section-title">THE PODCAST</h2>
      <p class="section-text">A new podcast series from the Centre for Market Structures at KLB brings researchers and practitioners together for open conversations on Strategy, Analytics, Economics and Leadership.</p>
    </div>
    <div class="section" style="top:240px">
      <h2 class="section-title">BE OUR GUEST</h2>
      <p class="section-text">Each episode runs about 30 minutes and is recorded on campus or remotely. We prepare the questions with you in advance, so you can share your experience with ease.</p>
    </div>
  </section>

  <section class="panel panel-intro">
    <svg class="shapes" viewBox="0 0 340 780" aria-hidden="true">
      <polygon points="0,10 132,10 0,132" fill="var(--lavender)"/>
      <polygon points="56,54 100,93 56,93" fill="var(--night)"/>
      <polygon points="340,473 340,780 60,780" fill="var(--royal)"/>
      <polygon points="173,566 262,650 173,650" fill="var(--night)"/>
    </svg>
    <div class="intro">
      <h1 class="intro-title">YOU ARE INVITED</h1>
      <p class="intro-text">The Centre for Market Structures at the business university KLB is launching a podcast series on Strategy, Analytics, Economics and Leadership. We would be delighted to welcome you as one of a small group of selected guests. Share your insights from practice, discuss current questions with our researchers and help shape a conversation that reaches students, alumni and decision makers. Find out more and register your interest at <span class="intro-link">www.klb.edu</span>.</p>
    </div>
  </section>

</main>
</body>
</html>
```